3 pages for Quillmoney.com (design required, not ecommerce coding)

We are a new start up specialising exclusively in enabling e-commerce in Africa so that African businesses can place a "buy now" button on products and services they offer on the internet. The mechanism that powers this is heavily grounded in mobile payments.

Because of this, the service will also be used for in-shop and person-to-person payments.

The main objective for looking for a professional design is to encourage people and business owners that land on the website from computers or web devices to be impressed by its appeal and message and then eventually sign up.

We would like to see good use of black fonts on yellow backgrounds in the design.

Website source code attached.

Target Market(s)

Africa - Countries like Ghana, Nigeria, Cameroon, Zimbabwe, South Africa, etc.

Industry/Entity Type

E-Commerce

Number of Pages Required

3 page

Font styles to use
Sans Serif

Requirements
Must have
• Key requirements of this design:
• 1. Suggest a simple text based logo
• 2. The design should be mobile responsive - current template is responsive
• 3. Pages:
• 1. Main Page: Should have a large graphic explaining our purpose. I have attached one we commissioned earlier. The final one should be bigger, maybe 940x400. Current illustrations shifted to the right and a large "Sign Up" button on the left. Under the graphic, should be a keyword heavy message to the visitor
• 2. Business and Shops page (business.php):
• Should have a large graphic maybe 940x400 illustrating the quillmoney to businesses. Narrative should be on the right. It should show a "Pay with Quillmoney" button and a click hovering and text to the right. This shows the narrative for online use. There should also be an illustration for in shop payments.
• The left of the graphic should be a larger "Sign Up" button for registering.
• 3. register page: registration requirements:
• 1. Mobile phone - text
• 2. Email address - text
• 3. City - drop down
• 4. Country - drop down
• 5. Password
• 6. Confirm Password
• Website source code attached.
Nice to have
• lots of yellow background... under black text ..
Should not have
• We are not big on flash.
• Also, this is not for ecommerce coding. we are more interested in the design.

```html
<!DOCTYPE html>
<html lang="en">
<head>
<meta charset="utf-8">
<title>Quillmoney</title>
<link href="https://fonts.googleapis.com/css2?family=Baumans&family=Ubuntu:wght@400;500;700&family=Reenie+Beanie&family=Source+Sans+3:ital,wght@0,400;0,600;0,700;1,700&display=swap" rel="stylesheet">
<style>
:root{
  --yellow:#fcd600;
  --yellow-deep:#e6be00;
  --yellow-pale:#ffe97a;
  --black:#1a1a1a;
  --charcoal:#333333;
  --panel:#f4f4f4;
  --line:#cfcfcf;
  --text:#333;
  --white:#ffffff;
}
*{box-sizing:border-box;margin:0;padding:0}
html,body{width:966px;height:1200px;overflow:hidden}
body{position:relative;background:var(--white);font-family:"Source Sans 3",Arial,sans-serif;color:var(--text)}
.abs{position:absolute}

/* header */
.site-header{left:0;top:0;width:966px;height:101px;background:var(--black)}
.brand{left:50px;top:28px;font-family:"Ubuntu",sans-serif;font-weight:500;font-size:32px;color:var(--yellow);display:flex;align-items:center;gap:10px}
.brand-mark{width:14px;height:14px;background:var(--yellow)}
.cart{left:729px;top:11px;width:197px;height:30px;background:#3a3a3a;color:var(--white);font-family:"Ubuntu",sans-serif;font-size:9px;display:flex;align-items:center;gap:8px;padding-left:10px}
.cart b{font-weight:500}
.main-nav{top:76px;left:0;width:966px;font-family:"Ubuntu",sans-serif;font-size:11px;color:var(--white)}
.main-nav a{position:absolute;top:0;color:var(--white);text-decoration:none;white-space:nowrap}
.main-nav a.active{color:var(--yellow)}

/* hero */
.hero{left:0;top:101px;width:966px;height:329px;background:var(--yellow)}
.signup{left:40px;top:16px;width:200px;height:298px;background:var(--panel);border-radius:3px;padding:6px 10px}
.signup h2{font-family:"Baumans",sans-serif;font-weight:400;color:var(--yellow);font-size:22px;margin:0 0 7px 3px}
.field{height:27px;border:1px solid var(--line);background:#e9e9e9;margin-bottom:9px;font-size:11px;color:#777;padding:0 6px;display:flex;align-items:center;justify-content:space-between}
.field svg{width:9px;height:7px}
.btn-signup{position:absolute;right:11px;bottom:13px;background:var(--black);color:var(--yellow);font-family:"Ubuntu",sans-serif;font-size:14px;padding:4px 9px;border-radius:5px}
.band{left:240px;top:159px;width:726px;height:11px;background:var(--yellow-deep)}
.step-num{top:36px;font-family:"Ubuntu",sans-serif;font-weight:700;font-size:44px;color:var(--yellow-pale);width:40px;text-align:center}
.step-photo{top:84px;width:156px;height:156px;border-radius:50%;border:5px solid var(--white);box-shadow:0 0 0 4px var(--yellow-deep)}
.caption{top:258px;width:170px;text-align:center;font-family:"Reenie Beanie",cursive;font-size:22px;line-height:19px;color:var(--black)}
.arrow{top:46px;width:64px;height:30px}

/* cards */
.card{top:460px;width:258px;height:194px;border:1px solid var(--line);border-radius:3px;background:var(--panel);padding:12px 13px;font-size:10.5px;line-height:14.5px}
.card.dark{background:var(--black);color:var(--white)}
.card h3{font-family:"Baumans",sans-serif;font-weight:400;color:var(--yellow-deep);font-size:24px;line-height:26px;margin-bottom:8px}
.card.dark h3{color:var(--yellow)}
.card p{margin-bottom:14px}
.card.dark p{font-weight:600}
.more{position:absolute;left:13px;bottom:10px;background:var(--black);color:var(--white);font-style:italic;font-weight:700;font-size:10px;padding:4px 6px;border-radius:3px}
.card.dark .more{background:var(--yellow);color:var(--black)}

/* intro */
.intro{left:56px;top:726px;width:582px;font-family:Arial,sans-serif;font-size:11.5px;line-height:16px;color:#444;text-align:justify}
.intro h1{font-family:"Baumans",sans-serif;font-weight:400;color:var(--yellow-deep);font-size:23px;line-height:30px;margin:0 0 10px 2px;text-align:left}
.intro h4{font-family:"Baumans",sans-serif;font-weight:400;color:var(--black);font-size:17px;margin:6px 0 2px}
.side-nav{left:687px;top:724px;width:228px;height:213px;background:var(--panel);border:1px solid #e4e4e4;border-radius:6px;overflow:hidden;font-family:"Ubuntu",sans-serif}
.side-nav h3{font-family:"Baumans",sans-serif;font-weight:400;color:var(--yellow-deep);font-size:23px;padding:8px 17px 6px}
.side-nav a{display:flex;justify-content:space-between;align-items:center;height:42px;padding:0 17px;font-size:14px;color:var(--black);text-decoration:none;border-top:1px solid #e2e2e2}
.side-nav a.active{background:#474747;color:var(--white)}
.side-nav svg{width:10px;height:12px}

/* gallery */
.gallery{left:0;top:976px;width:966px;height:165px;background:var(--yellow)}
.thumb{top:25px;width:157px;height:109px;border:2px solid #d8c685;background:linear-gradient(135deg,#8a6a4a,#4c3b2c 60%,#2a2522)}
.thumb.light{background:linear-gradient(135deg,#ecdcc8,#c9a98d 60%,#a48468)}
.gallery-arrow{top:62px;width:16px;height:26px}

/* footer */
.site-footer{left:0;top:1141px;width:966px;height:59px;background:var(--charcoal);color:var(--white);font-family:"Ubuntu",sans-serif;font-size:11px}
.site-footer span{position:absolute;top:26px}
</style>
</head>
<body>

<header class="site-header abs">
  <div class="brand abs"><span class="brand-mark"></span>Quillmoney</div>
  <div class="cart abs">
    <svg width="24" height="20" viewBox="0 0 24 20"><path d="M1 2h4l3 11h11l3-8H7" fill="none" stroke="#fff" stroke-width="1.6"/><circle cx="9" cy="17" r="1.6" fill="#fff"/><circle cx="18" cy="17" r="1.6" fill="#fff"/></svg>
    <span><b>My Cart :</b>&nbsp; 1 Item(s) &nbsp;|&nbsp; $ 250 (AUD)</span>
  </div>
  <nav class="main-nav abs">
    <a class="active" style="left:347px">HOME</a>
    <a style="left:412px">BUSINESS &amp; SHOPS</a>
    <a style="left:544px">ADD MONEY</a>
    <a style="left:638px">PAY SOMEONE</a>
    <a style="left:745px">RECEIVE MONEY</a>
    <a style="left:860px">MY ACCOUNT</a>
  </nav>
</header>

<section class="hero abs">
  <div class="band abs"></div>
  <form class="signup abs">
    <h2>Sign Up</h2>
    <div class="field">Mobile phone</div>
    <div class="field">Email Address</div>
    <div class="field">City <svg viewBox="0 0 9 7"><path d="M0 0h9L4.5 7z" fill="#222"/></svg></div>
    <div class="field">Country <svg viewBox="0 0 9 7"><path d="M0 0h9L4.5 7z" fill="#222"/></svg></div>
    <div class="field">Password</div>
    <div class="field">Confirm Password</div>
    <span class="btn-signup">SIGN UP</span>
  </form>

  <div class="step-num abs" style="left:321px">1</div>
  <div class="step-num abs" style="left:483px">2</div>
  <div class="step-num abs" style="left:647px">3</div>
  <div class="step-num abs" style="left:812px">4</div>

  <svg class="arrow abs" style="left:385px" viewBox="0 0 64 30"><path d="M3 22C14 2 40 2 56 24" fill="none" stroke="#1a1a1a" stroke-width="2"/><path d="M47 22l9 3 0-10" fill="none" stroke="#1a1a1a" stroke-width="2"/></svg>
  <svg class="arrow abs" style="left:556px" viewBox="0 0 64 30"><path d="M3 22C14 2 40 2 56 24" fill="none" stroke="#1a1a1a" stroke-width="2"/><path d="M47 22l9 3 0-10" fill="none" stroke="#1a1a1a" stroke-width="2"/></svg>
  <svg class="arrow abs" style="left:718px" viewBox="0 0 64 30"><path d="M3 22C14 2 40 2 56 24" fill="none" stroke="#1a1a1a" stroke-width="2"/><path d="M47 22l9 3 0-10" fill="none" stroke="#1a1a1a" stroke-width="2"/></svg>

  <div class="step-photo abs" style="left:258px;background:radial-gradient(circle at 40% 45%,#b07a5a,#6b4a3a 60%,#c8b8a8)" role="img" aria-label="Woman adding money to her account on a mobile phone"></div>
  <div class="step-photo abs" style="left:428px;background:radial-gradient(circle at 45% 50%,#e8dcd4,#c9b2a4 60%,#f2eeea)" role="img" aria-label="Woman paying online with a card and laptop"></div>
  <div class="step-photo abs" style="left:598px;background:radial-gradient(circle at 55% 45%,#3a6fc4,#d8c8b0 55%,#ece4d8)" role="img" aria-label="Courier with a parcel next to a wall clock"></div>
  <div class="step-photo abs" style="left:767px;background:radial-gradient(circle at 45% 55%,#d4a868,#b8a898 55%,#e4e0dc)" role="img" aria-label="Customer receiving a delivered parcel"></div>

  <div class="caption abs" style="left:243px">Add money to<br>your account</div>
  <div class="caption abs" style="left:416px">Pay online<br>Buy in shops</div>
  <div class="caption abs" style="left:598px">Service and goods<br>delivery guaranteed</div>
  <div class="caption abs" style="left:772px;top:268px">Enjoy!</div>
</section>

<article class="card dark abs" style="left:60px">
  <h3>About</h3>
  <p>Lorem ipsum dolor sit amet, consectetuer adipiscing elit, sed diam nonummy nibh euis-mod tincidunt ut laoreet dolore magna aliquam erat volutpat</p>
  <p><strong>nonummy nibh euismod</strong> tincidunt ut laoreet dolore magna aliquam erat volutpat...</p>
  <span class="more">Read More ››</span>
</article>
<article class="card abs" style="left:356px">
  <h3>Company</h3>
  <p>Lorem ipsum dolor sit amet, consectetuer adipiscing elit, sed diam nonummy nibh euis-mod tincidunt ut laoreet dolore magna aliquam erat volutpat</p>
  <p><strong>nonummy nibh euismod</strong> tincidunt ut laoreet dolore magna aliquam erat volutpat...</p>
  <span class="more">Read More ››</span>
</article>
<article class="card abs" style="left:653px">
  <h3>Services</h3>
  <p>Lorem ipsum dolor sit amet, consectetuer adipiscing elit, sed diam nonummy nibh euis-mod tincidunt ut laoreet dolore magna aliquam erat volutpat</p>
  <p><strong>nonummy nibh euismod</strong> tincidunt ut laoreet dolore magna aliquam erat volutpat...</p>
  <span class="more">Read More ››</span>
</article>

<section class="intro abs">
  <h1>Consectetuer adipiscing elit, sed diam nonummy.</h1>
  <p><b><i>Lorem ipsum dolor sit amet, consectetuer adipiscing elit, sed diam nonummy nibh euismod tincid-unt ut laoreet dolore magna aliquam erat volutpat.</i></b> Lorem ipsum dolor sit amet, consectetuer adipiscing elit, sed diam nonummy nibh euismod tincidunt ut laoreet dolore magna aliquam erat volutpat. Ut wisi enim ad minim veniam, quis nostrud exerci tation ullamcorper suscipit..</p>
  <h4>Sub Header</h4>
  <p>Ut wisi enim ad minim veniam, quis nostrud exerci tation ullamcorper nibh euismod tincidunt ut laoreet dolore magna aliquam suscipit lobortis nisl ut aliquip ex ea commodo consequat.tation ullamcorper nibh euismod tincidunt ut laoreet dolore magna aliquam suscipit lobortis nisl ut aliquip ex ea commodo conse-quat tation ullamcorper nibh euismod tincidunt ut laoreet.....</p>
</section>

<nav class="side-nav abs">
  <h3>Navigation</h3>
  <a>›› Home</a>
  <a class="active">›› Product <svg viewBox="0 0 10 12"><path d="M2 1l6 5-6 5" fill="none" stroke="#fff" stroke-width="2.4"/></svg></a>
  <a>›› Company <svg viewBox="0 0 10 12"><path d="M2 1l6 5-6 5" fill="none" stroke="#1a1a1a" stroke-width="2.4"/></svg></a>
  <a>›› Contact</a>
</nav>

<section class="gallery abs">
  <svg class="gallery-arrow abs" style="left:80px" viewBox="0 0 16 26"><path d="M13 2L4 13l9 11" fill="none" stroke="#1a1a1a" stroke-width="4"/></svg>
  <div class="thumb abs" style="left:110px" role="img" aria-label="Laptop, notebook and coffee on a wooden desk"></div>
  <div class="thumb light abs" style="left:299px" role="img" aria-label="Desk seen from above with books, phone and stationery"></div>
  <div class="thumb abs" style="left:494px;background:linear-gradient(135deg,#6a5a4a,#2e2a28 55%,#1a1a1a)" role="img" aria-label="Person working on a laptop at a table"></div>
  <div class="thumb abs" style="left:691px" role="img" aria-label="Laptop, notebook and coffee on a wooden desk"></div>
  <svg class="gallery-arrow abs" style="left:870px" viewBox="0 0 16 26"><path d="M3 2l9 11-9 11" fill="none" stroke="#1a1a1a" stroke-width="4"/></svg>
</section>

<footer class="site-footer abs">
  <span style="left:87px">© 2014 Brightmark, All Rights Reserved</span>
  <span style="right:92px">Design and coding by Brightmark</span>
</footer>

</body>
</html>
```